Webdesign für berufliches Schulzentrum für Ernährung, Gastgewerbe, Gesundheit
Zielgruppe
Berufliches Schulzentrum für Ernährung, Gastgewerbe, Gesundheit
Zielgruppe: Schüler und Auszubildende
Aufgabenstellung
- modernes, aber dennoch strukturiertes Aussehen der Webseite
- einfache Navigation
- die beiden Grüntöne aus dem Logo sollen sich bitte in der Seite wiederfinden - jedoch in freundlicher Form

```html
<!DOCTYPE html>
<html lang="de">
<head>
<meta charset="utf-8">
<title>BSZ Lindenhain – Webdesign</title>
<link rel="stylesheet" href="https://fonts.googleapis.com/css2?family=Montserrat:wght@300;400;500;600;700&display=swap">
<style>
:root{
  --stage:#e8e8e8;
  --white:#ffffff;
  --ink:#1e2a22;
  --ink-soft:#5c6660;
  --mint:#c6ecd2;
  --forest:#2f4437;
  --forest-mid:#4c6352;
  --label:rgba(150,156,150,.62);
  --rule:#c9cfcb;
  --accent-red:#d8282f;
}
*{box-sizing:border-box;margin:0;padding:0}
h1,h2,h3{font-weight:400}
html,body{width:923px;height:1200px;overflow:hidden;background:var(--stage);font-family:"Montserrat",sans-serif;color:var(--ink)}
.view{position:absolute;overflow:hidden;background:var(--white)}
.view--full{left:65px;top:80px;width:273px;height:1042px;box-shadow:0 4px 14px rgba(0,0,0,.18)}
.view--zoom{left:396px;top:0;width:472px;height:1200px}
.page{position:absolute;left:0;top:0;width:860px;height:3276px;transform-origin:0 0;background:var(--white)}
.view--full .page{transform:scale(.3179)}
.view--zoom .page{transform:scale(.549) translateY(-679px)}
.abs{position:absolute}

/* nav */
.nav{left:0;top:0;width:860px;height:62px;background:var(--white);border-bottom:1px solid #eee}
.brand{left:14px;top:14px;display:flex;align-items:center;gap:8px;font-size:11px;font-weight:600;color:var(--forest)}
.brand-mark{width:22px;height:22px;background:var(--forest-mid)}
.menu{left:142px;top:26px;display:flex;gap:14px;font-size:7.5px;font-weight:600;letter-spacing:1.1px;white-space:nowrap}
.menu span:first-child{border-bottom:1px solid var(--ink)}
.burger{left:830px;top:22px;width:16px}
.burger i{display:block;height:2px;background:var(--ink-soft);margin-bottom:4px}

/* hero */
.hero{left:0;top:62px;width:860px;height:423px;background:linear-gradient(160deg,#8a9385 0%,#66775f 45%,#4b5f4c 100%)}
.hero-title{left:0;top:103px;width:860px;text-align:center;font-size:30px;letter-spacing:4px;color:var(--white);line-height:49px}
.hero-title span{background:var(--label);padding:0 6px}
.hero-sub{left:200px;top:263px;width:460px;text-align:center;font-size:10px;font-weight:700;color:var(--white);line-height:15px}
.hero-btn{left:361px;top:314px;width:147px;height:33px;background:var(--white);font-size:9px;font-weight:700;letter-spacing:1px;display:flex;align-items:center;justify-content:center}
.hero-social{left:22px;top:396px;width:16px;height:16px;border:2px solid var(--white);border-radius:4px}
.hero-badge{left:713px;top:343px;width:116px;height:52px}
.hero-badge .b-circle{left:0;top:0;width:52px;height:52px;border-radius:50%;background:var(--white);border:3px solid var(--accent-red)}
.hero-badge .b-rect{left:52px;top:10px;width:64px;height:30px;background:var(--accent-red)}

/* buttons */
.btn{position:absolute;background:var(--mint);font-size:10px;font-weight:600;letter-spacing:1.6px;display:flex;align-items:center;justify-content:center;color:var(--ink);box-shadow:2px 2px 0 rgba(0,0,0,.08);white-space:nowrap}

/* intro */
.rule{position:absolute;height:1px;background:var(--rule)}
.intro-photo{left:419px;top:553px;width:441px;height:326px;background:linear-gradient(180deg,#dfe6ec 0%,#c8ccd0 55%,#7f9471 100%)}
.intro-head{left:59px;top:597px;font-size:22px;letter-spacing:2px;line-height:38px;white-space:nowrap}
.intro-head span{display:inline-block;background:var(--white);border:1px solid var(--rule);padding:0 8px}
.intro-text{left:67px;top:687px;width:345px;font-size:10.5px;line-height:16.2px;letter-spacing:.4px}

/* school types */
.dark{left:0;width:860px}
.types{top:946px;height:504px;background:radial-gradient(ellipse at 50% 60%,#60705f 0%,#3a4c3e 60%,#283a2e 100%)}
.types-kicker{left:0;top:56px;width:860px;text-align:center;color:var(--white);font-size:12px;font-weight:600;letter-spacing:1px}
.label-box{position:absolute;background:var(--label);color:var(--white);letter-spacing:4px;font-weight:400}
.types-title{left:203px;top:76px;width:463px;height:40px;font-size:30px;display:flex;align-items:center;justify-content:center}
.card{position:absolute;top:158px;width:224px;height:283px;background:var(--white);text-align:center;box-shadow:0 2px 6px rgba(0,0,0,.2)}
.card-img{height:113px}
.card h3{font-size:13px;font-weight:700;letter-spacing:3px;margin:14px 0 10px}
.card p{font-size:11.5px;line-height:19px;letter-spacing:.8px;color:var(--ink-soft)}
.c1{left:56px}.c1 .card-img{background:linear-gradient(135deg,#e9a9bf,#f2e6da 55%,#8b4a3a)}
.c2{left:325px}.c2 .card-img{background:linear-gradient(135deg,#3d3a36,#e8dccb 55%,#6d6a61)}
.c3{left:592px}.c3 .card-img{background:linear-gradient(135deg,#7f8aa0,#d8c0b0 55%,#eef1f4)}

/* plans */
.plans-h{position:absolute;font-size:19px;letter-spacing:2.5px;white-space:nowrap}
.plans-art{left:327px;top:1484px;width:533px;height:360px;border-radius:180px 180px 40px 40px;background:radial-gradient(ellipse at 50% 55%,#f4f3f8 0%,#dfe3f2 45%,#c8ecd3 75%,#eef2f8 100%)}

/* news */
.news{top:1879px;height:510px;background:linear-gradient(120deg,#6d7d6c 0%,#4f6453 50%,#3f5443 100%)}
.news-title{left:0;top:40px;width:256px;height:40px;font-size:32px;padding-left:62px;display:flex;align-items:center}
.news-card{left:169px;top:108px;width:538px;height:347px;background:var(--white)}
.news-photo{left:0;top:0;width:275px;height:347px;background:linear-gradient(160deg,#5c5d55 0%,#2c2d2a 50%,#8a7c5d 100%)}
.news-date{left:303px;top:66px;font-size:10px;letter-spacing:1.4px;padding-bottom:6px;border-bottom:1px solid var(--rule);width:164px}
.news-head{left:303px;top:117px;font-size:21px;letter-spacing:2.2px;line-height:22.5px;white-space:nowrap}
.arrow{position:absolute;width:26px;height:26px;border:1.5px solid var(--white);border-radius:50%}
.arrow svg{position:absolute;left:6px;top:6px}
.dots{left:420px;top:478px;display:flex;gap:3px}
.dots i{width:7px;height:7px;border:1px solid var(--white);border-radius:50%}
.dots i:first-child{background:var(--white)}

/* support */
.support-art{left:0;top:2414px;width:454px;height:373px;border-radius:0 200px 0 0;background:radial-gradient(ellipse at 50% 55%,#f6a695 0%,#f3c2b0 35%,#d6efdd 70%,#ffffff 100%)}
.support-text{left:466px;top:2518px;font-size:15px;letter-spacing:2px;line-height:26.5px;white-space:nowrap}
.support-text span{display:inline-block;border:1px solid #e3e6e4;padding:0 6px;line-height:24px}
.support-q{left:472px;top:2660px;font-size:12px;letter-spacing:1.6px;line-height:16px;white-space:nowrap}

/* contact */
.contact{left:0;top:2787px;width:860px;height:489px;background:linear-gradient(110deg,#4c6a52 0%,#6f9275 45%,#a9c7ad 80%,#c8ddc9 100%)}
.contact-title{left:0;top:100px;font-size:26px;line-height:40px;color:var(--white);letter-spacing:3px;white-space:nowrap}
.contact-title span{display:inline-block;background:var(--label);padding:0 8px 0 46px}
.contact-info{left:48px;top:194px;width:250px;font-size:9.5px;line-height:13px;color:var(--white);font-weight:500}
.contact-info p{margin-bottom:10px}
.field{position:absolute;background:rgba(255,255,255,.88);font-size:9px;padding:6px 10px;color:var(--ink-soft)}
.contact-btn{left:342px;top:360px;width:147px;height:28px}
.legal{left:689px;top:462px;display:flex;gap:24px;font-size:9px;color:rgba(255,255,255,.8)}
</style>
</head>
<body>

<div class="view view--full">
  <div class="page">
    <header class="nav abs">
      <div class="brand abs"><span class="brand-mark"></span>BSZ Lindenhain</div>
      <nav class="menu abs"><span>ÜBER UNS</span><span>SCHULARTEN</span><span>PLÄNE/TERMINE</span><span>AKTUELLES</span><span>SCHULANMELDUNG</span><span>IMPRESSION</span><span>FÖRDERVEREIN</span><span>KONTAKT</span></nav>
      <div class="burger abs"><i></i><i></i><i></i></div>
    </header>
    <section class="hero abs" role="img" aria-label="Foto des Schulgebäudes mit grüner Überlagerung">
      <h1 class="hero-title abs"><span>HERZLICH WILLKOMMEN</span><br><span>an unserem BSZ für</span><br><span>Ernährung, Gastgewerbe, Gesundheit!</span></h1>
      <p class="hero-sub abs">Offizielle Seite des Beruflichen Schulzentrums Lindenhain für Ausbildung und Beruf: Bildung schafft Zukunft.</p>
      <div class="hero-btn abs">Mehr erfahren.</div>
      <div class="hero-social abs"></div>
      <div class="hero-badge abs"><div class="b-circle abs"></div><div class="b-rect abs"></div></div>
    </section>
    <section>
      <div class="rule" style="left:0;top:553px;width:352px"></div>
      <div class="intro-photo abs" role="img" aria-label="Foto des historischen Schulgebäudes mit Bäumen"></div>
      <h2 class="intro-head abs"><span>Unsere Schule ist seit über 100 Jahren</span><br><span>die Adresse für kompetente Bildung.</span></h2>
      <p class="intro-text abs">Sie lernen Berufe wie: Bäcker/-in, Konditor/-in, Fachverkäufer/-in im Lebensmittelhandwerk, Koch/Köchin, Restaurantfachmann/-frau, Fachkraft im Gastgewerbe, Fachmann/-frau für System- gastronomie, Hotelfachmann/-frau und Pharmazeutisch-technische/-r Assistent/-in. Förderschüler bereiten wir auf den Beruf Fach- praktiker/-in im Bäckerhandwerk vor.</p>
      <div class="btn" style="left:64px;top:820px;width:120px;height:31px">Mehr erfahren</div>
    </section>
    <section class="dark types abs">
      <p class="types-kicker abs">Berufsschule - Beruftsfachschule - Berufsvorbereitung</p>
      <h2 class="label-box types-title">UNSERE SCHULARTEN.</h2>
      <article class="card c1"><div class="card-img" role="img" aria-label="Foto einer verzierten Torte"></div><h3>ERNÄHRUNG</h3><p>Bäcker/in<br>Konditor/in<br>Fachverkäufer/in Bäckerei<br>Fachverkäufer/in Fleischerei<br>Fachpraktiker/-in Bäckerei</p></article>
      <article class="card c2"><div class="card-img" role="img" aria-label="Foto einer Köchin beim Würzen"></div><h3>GASTGEWERBE</h3><p>Koch/Köchin<br>Hotelfachmann/-frau<br>Restaurantfachmann/-frau<br>Fachmann/-frau für<br>Systemgastronomie<br>Fachkraft im Gastgewerbe</p></article>
      <article class="card c3"><div class="card-img" role="img" aria-label="Foto von Händen in der Pflege"></div><h3>GESUNDHEIT</h3><p>Informationen<br>Pharmazeutisch-technische/r<br>Assistent/in<br><br>Flyer Ausbildung PTA<br>Flyer Schnupperkurs</p></article>
    </section>
    <section>
      <h2 class="plans-h" style="left:67px;top:1514px">Nachschreibetermine</h2>
      <div class="rule" style="left:0;top:1549px;width:294px"></div>
      <div class="btn" style="left:145px;top:1570px;width:150px;height:31px">2. Halbjahr 2023/24</div>
      <div class="btn" style="left:145px;top:1621px;width:150px;height:31px">1. Halbjahr 2023/24</div>
      <h2 class="plans-h" style="left:151px;top:1672px">Blockpläne</h2>
      <div class="rule" style="left:0;top:1707px;width:293px"></div>
      <div class="btn" style="left:148px;top:1728px;width:150px;height:31px">2024/2025</div>
      <div class="btn" style="left:148px;top:1779px;width:150px;height:31px">2023/2024</div>
      <div class="plans-art abs" role="img" aria-label="Illustration einer Person vor einem großen Kalender mit Papierfliegern"></div>
    </section>
    <section class="dark news abs">
      <h2 class="label-box news-title">Aktuelles</h2>
      <div class="arrow" style="left:118px;top:267px"><svg width="12" height="12" viewBox="0 0 12 12"><path d="M10 6H2M5 3 2 6l3 3" stroke="#fff" fill="none" stroke-width="1.2"/></svg></div>
      <div class="arrow" style="left:727px;top:244px"><svg width="12" height="12" viewBox="0 0 12 12"><path d="M2 6h8M7 3l3 3-3 3" stroke="#fff" fill="none" stroke-width="1.2"/></svg></div>
      <article class="news-card abs">
        <div class="news-photo abs" role="img" aria-label="Foto eines Kochteams mit Pokalen und Urkunden"></div>
        <p class="news-date abs">September 2023</p>
        <h3 class="news-head abs">Rinderbäckchen<br>zwischen<br>Bauernprotesten<br>und Bahnstreik</h3>
        <div class="btn" style="left:301px;top:235px;width:120px;height:32px">Mehr erfahren</div>
      </article>
      <div class="dots abs"><i></i><i></i><i></i><i></i><i></i></div>
    </section>
    <section>
      <div class="support-art abs" role="img" aria-label="Illustration zweier Hände, die kleine Menschen und Pflanzen tragen"></div>
      <div class="rule" style="left:487px;top:2459px;width:373px"></div>
      <p class="support-text abs"><span>Seit 1997 unterstützt uns der Verein</span><br><span>"Freunde und Förderer des</span><br><span>Beruflichen Schulzentrums</span><br><span>Lindenhain e.V.".</span></p>
      <p class="support-q abs">Möchtest auch du unser berufliches<br>Schulzentrum unterstützen?</p>
      <div class="btn" style="left:466px;top:2704px;width:120px;height:31px">Mehr erfahren</div>
    </section>
    <footer class="contact abs" role="group" aria-label="Kontakt">
      <h2 class="contact-title abs"><span>Wir freuen uns</span><br><span>auf Ihre Anfrage.</span></h2>
      <div class="contact-info abs">
        <p><b>BSZ Lindenhain</b><br>Gartenweg 12,<br>01234 Lindenhain</p>
        <p>Telefon: 0123 / 45 67 8-0<br>Telefax: 0123 / 45 67 8-42</p>
        <p>E-Mail: info@bsz-lindenhain.de</p>
        <p>Öffnungszeiten:<br>Mo bis Do 07:30 Uhr bis 12:00 Uhr /<br>12:45 Uhr bis 15:00 Uhr<br>sowie Fr 07:30 Uhr bis 12:30 Uhr</p>
        <p>▢ @bsz_lindenhain</p>
      </div>
      <div class="field" style="left:342px;top:157px;width:138px;height:26px">Name</div>
      <div class="field" style="left:489px;top:157px;width:138px;height:26px">Nachname</div>
      <div class="field" style="left:342px;top:199px;width:282px;height:26px">E-Mail Adresse</div>
      <div class="field" style="left:632px;top:199px;width:123px;height:26px">Telefon</div>
      <div class="field" style="left:342px;top:240px;width:413px;height:93px">Nachricht</div>
      <div class="btn contact-btn">Kontaktieren</div>
      <div class="legal abs"><span>Datenschutz</span><span>Impressum</span></div>
    </footer>
  </div>
</div>

<div class="view view--zoom">
  <div class="page">
    <header class="nav abs">
      <div class="brand abs"><span class="brand-mark"></span>BSZ Lindenhain</div>
      <nav class="menu abs"><span>ÜBER UNS</span><span>SCHULARTEN</span><span>PLÄNE/TERMINE</span><span>AKTUELLES</span><span>SCHULANMELDUNG</span><span>IMPRESSION</span><span>FÖRDERVEREIN</span><span>KONTAKT</span></nav>
      <div class="burger abs"><i></i><i></i><i></i></div>
    </header>
    <section class="hero abs" role="img" aria-label="Foto des Schulgebäudes mit grüner Überlagerung">
      <h1 class="hero-title abs"><span>HERZLICH WILLKOMMEN</span><br><span>an unserem BSZ für</span><br><span>Ernährung, Gastgewerbe, Gesundheit!</span></h1>
      <p class="hero-sub abs">Offizielle Seite des Beruflichen Schulzentrums Lindenhain für Ausbildung und Beruf: Bildung schafft Zukunft.</p>
      <div class="hero-btn abs">Mehr erfahren.</div>
      <div class="hero-social abs"></div>
      <div class="hero-badge abs"><div class="b-circle abs"></div><div class="b-rect abs"></div></div>
    </section>
    <section>
      <div class="rule" style="left:0;top:553px;width:352px"></div>
      <div class="intro-photo abs" role="img" aria-label="Foto des historischen Schulgebäudes mit Bäumen"></div>
      <h2 class="intro-head abs"><span>Unsere Schule ist seit über 100 Jahren</span><br><span>die Adresse für kompetente Bildung.</span></h2>
      <p class="intro-text abs">Sie lernen Berufe wie: Bäcker/-in, Konditor/-in, Fachverkäufer/-in im Lebensmittelhandwerk, Koch/Köchin, Restaurantfachmann/-frau, Fachkraft im Gastgewerbe, Fachmann/-frau für System- gastronomie, Hotelfachmann/-frau und Pharmazeutisch-technische/-r Assistent/-in. Förderschüler bereiten wir auf den Beruf Fach- praktiker/-in im Bäckerhandwerk vor.</p>
      <div class="btn" style="left:64px;top:820px;width:120px;height:31px">Mehr erfahren</div>
    </section>
    <section class="dark types abs">
      <p class="types-kicker abs">Berufsschule - Beruftsfachschule - Berufsvorbereitung</p>
      <h2 class="label-box types-title">UNSERE SCHULARTEN.</h2>
      <article class="card c1"><div class="card-img" role="img" aria-label="Foto einer verzierten Torte"></div><h3>ERNÄHRUNG</h3><p>Bäcker/in<br>Konditor/in<br>Fachverkäufer/in Bäckerei<br>Fachverkäufer/in Fleischerei<br>Fachpraktiker/-in Bäckerei</p></article>
      <article class="card c2"><div class="card-img" role="img" aria-label="Foto einer Köchin beim Würzen"></div><h3>GASTGEWERBE</h3><p>Koch/Köchin<br>Hotelfachmann/-frau<br>Restaurantfachmann/-frau<br>Fachmann/-frau für<br>Systemgastronomie<br>Fachkraft im Gastgewerbe</p></article>
      <article class="card c3"><div class="card-img" role="img" aria-label="Foto von Händen in der Pflege"></div><h3>GESUNDHEIT</h3><p>Informationen<br>Pharmazeutisch-technische/r<br>Assistent/in<br><br>Flyer Ausbildung PTA<br>Flyer Schnupperkurs</p></article>
    </section>
    <section>
      <h2 class="plans-h" style="left:67px;top:1514px">Nachschreibetermine</h2>
      <div class="rule" style="left:0;top:1549px;width:294px"></div>
      <div class="btn" style="left:145px;top:1570px;width:150px;height:31px">2. Halbjahr 2023/24</div>
      <div class="btn" style="left:145px;top:1621px;width:150px;height:31px">1. Halbjahr 2023/24</div>
      <h2 class="plans-h" style="left:151px;top:1672px">Blockpläne</h2>
      <div class="rule" style="left:0;top:1707px;width:293px"></div>
      <div class="btn" style="left:148px;top:1728px;width:150px;height:31px">2024/2025</div>
      <div class="btn" style="left:148px;top:1779px;width:150px;height:31px">2023/2024</div>
      <div class="plans-art abs" role="img" aria-label="Illustration einer Person vor einem großen Kalender mit Papierfliegern"></div>
    </section>
    <section class="dark news abs">
      <h2 class="label-box news-title">Aktuelles</h2>
      <div class="arrow" style="left:118px;top:267px"><svg width="12" height="12" viewBox="0 0 12 12"><path d="M10 6H2M5 3 2 6l3 3" stroke="#fff" fill="none" stroke-width="1.2"/></svg></div>
      <div class="arrow" style="left:727px;top:244px"><svg width="12" height="12" viewBox="0 0 12 12"><path d="M2 6h8M7 3l3 3-3 3" stroke="#fff" fill="none" stroke-width="1.2"/></svg></div>
      <article class="news-card abs">
        <div class="news-photo abs" role="img" aria-label="Foto eines Kochteams mit Pokalen und Urkunden"></div>
        <p class="news-date abs">September 2023</p>
        <h3 class="news-head abs">Rinderbäckchen<br>zwischen<br>Bauernprotesten<br>und Bahnstreik</h3>
        <div class="btn" style="left:301px;top:235px;width:120px;height:32px">Mehr erfahren</div>
      </article>
      <div class="dots abs"><i></i><i></i><i></i><i></i><i></i></div>
    </section>
    <section>
      <div class="support-art abs" role="img" aria-label="Illustration zweier Hände, die kleine Menschen und Pflanzen tragen"></div>
      <div class="rule" style="left:487px;top:2459px;width:373px"></div>
      <p class="support-text abs"><span>Seit 1997 unterstützt uns der Verein</span><br><span>"Freunde und Förderer des</span><br><span>Beruflichen Schulzentrums</span><br><span>Lindenhain e.V.".</span></p>
      <p class="support-q abs">Möchtest auch du unser berufliches<br>Schulzentrum unterstützen?</p>
      <div class="btn" style="left:466px;top:2704px;width:120px;height:31px">Mehr erfahren</div>
    </section>
    <footer class="contact abs" role="group" aria-label="Kontakt">
      <h2 class="contact-title abs"><span>Wir freuen uns</span><br><span>auf Ihre Anfrage.</span></h2>
      <div class="contact-info abs">
        <p><b>BSZ Lindenhain</b><br>Gartenweg 12,<br>01234 Lindenhain</p>
        <p>Telefon: 0123 / 45 67 8-0<br>Telefax: 0123 / 45 67 8-42</p>
        <p>E-Mail: info@bsz-lindenhain.de</p>
        <p>Öffnungszeiten:<br>Mo bis Do 07:30 Uhr bis 12:00 Uhr /<br>12:45 Uhr bis 15:00 Uhr<br>sowie Fr 07:30 Uhr bis 12:30 Uhr</p>
        <p>▢ @bsz_lindenhain</p>
      </div>
      <div class="field" style="left:342px;top:157px;width:138px;height:26px">Name</div>
      <div class="field" style="left:489px;top:157px;width:138px;height:26px">Nachname</div>
      <div class="field" style="left:342px;top:199px;width:282px;height:26px">E-Mail Adresse</div>
      <div class="field" style="left:632px;top:199px;width:123px;height:26px">Telefon</div>
      <div class="field" style="left:342px;top:240px;width:413px;height:93px">Nachricht</div>
      <div class="btn contact-btn">Kontaktieren</div>
      <div class="legal abs"><span>Datenschutz</span><span>Impressum</span></div>
    </footer>
  </div>
</div>

</body>
</html>
```